card design for engineering consultancy

engineering drafting and project management company the provides drafting services for.
Electrical, Hydraulic, Mechanical, and Civil services
The company is called Q7R Services and logo is as attached
Information on card should be.
1. Logo
2.website : Q7RServices.example
3. email : info@Q7RServices.example
4. Phone: (+61) 400512836
5. Motto: Design - Document - Develop - Deliver

this card should be basically used for business identification only

Target Market(s)

electricians plumbers air conditioning installers and civil contractors

Industry/Entity Type

engineering, drafting, electrical, plumbing, airconditioning, civil

Contact Information for Business Card

1. Logo 2.website : Q7RServices.example 3. email : info@Q7RServices.example 4. Phone: (+61) 400512836 5. Motto: Design - Document - Develop - Deliver

Font styles to use
Serif

Requirements
Must have
• logo
Nice to have
• something inovative and different that makes it stand out from being just another business card

```html
<!DOCTYPE html>
<html lang="en">
<head>
<meta charset="utf-8">
<title>Q7R Services – Business Card</title>
<link href="https://fonts.googleapis.com/css2?family=Quicksand:wght@400;600&display=swap" rel="stylesheet">
<style>
  :root {
    --page-bg: #d4d4d4;
    --card-bg: #0d0d0d;
    --frame: #bdbdbd;
    --brand-grey: #5a5858;
    --accent-red: #d11a24;
    --text-grey: #a9a9a9;
    --rule: #3a3a3a;
  }
  * { box-sizing: border-box; margin: 0; padding: 0; }
  html, body {
    width: 1200px; height: 900px; overflow: hidden;
    background: var(--page-bg);
    font-family: "Quicksand", sans-serif;
  }
  .sheet {
    width: 1200px; height: 900px;
    display: flex; flex-direction: column;
    align-items: center; justify-content: center; gap: 40px;
  }
  .card {
    position: relative;
    width: 700px; height: 400px;
    background: var(--card-bg);
    box-shadow: 0 8px 24px rgba(0,0,0,.25);
  }
  .card__frame {
    position: absolute; inset: 10px;
    border: 1.5px solid var(--frame);
  }
  .brand {
    display: flex; align-items: center; gap: 18px;
    color: var(--brand-grey);
    font-weight: 600;
    letter-spacing: 4px;
    text-transform: uppercase;
  }
  .brand__mark {
    width: 34px; height: 34px;
    background: var(--accent-red);
  }
  .card--front .brand {
    position: absolute; left: 0; right: 0; top: 50%;
    transform: translateY(-50%);
    justify-content: center;
    font-size: 52px;
  }
  .card--back .brand {
    position: absolute; left: 0; right: 0; top: 95px;
    justify-content: center;
    font-size: 40px;
  }
  .card--back .brand__mark { width: 28px; height: 28px; }
  .motto {
    position: absolute; left: 50px; right: 50px; top: 220px;
    text-align: center;
    color: var(--accent-red);
    font-size: 22px;
    letter-spacing: 7px;
  }
  .divider {
    position: absolute; left: 40px; right: 40px; top: 280px;
    border-top: 1px solid var(--rule);
  }
  .contacts {
    position: absolute; left: 40px; right: 40px; top: 300px;
    display: flex; justify-content: space-between; align-items: center;
    list-style: none;
    color: var(--text-grey);
    font-size: 15px;
    letter-spacing: .5px;
  }
  .contacts__item { display: flex; align-items: center; gap: 8px; }
  .contacts__icon { width: 16px; height: 16px; flex: none; }
</style>
</head>
<body>
<main class="sheet">

  <section class="card card--front" aria-label="Card front">
    <div class="card__frame"></div>
    <div class="brand"><span class="brand__mark"></span><span class="brand__name">Q7R Services</span></div>
  </section>

  <section class="card card--back" aria-label="Card back">
    <div class="card__frame"></div>
    <div class="brand"><span class="brand__mark"></span><span class="brand__name">Q7R Services</span></div>
    <p class="motto">Document - Develop - Deliver</p>
    <div class="divider"></div>
    <ul class="contacts">
      <li class="contacts__item">
        <svg class="contacts__icon" viewBox="0 0 24 24" aria-hidden="true">
          <path fill="#d11a24" d="M6.6 10.8a15.1 15.1 0 0 0 6.6 6.6l2.2-2.2a1 1 0 0 1 1-.25 11.4 11.4 0 0 0 3.6.57 1 1 0 0 1 1 1V20a1 1 0 0 1-1 1A17 17 0 0 1 3 4a1 1 0 0 1 1-1h3.5a1 1 0 0 1 1 1c0 1.25.2 2.45.57 3.57a1 1 0 0 1-.25 1z"/>
        </svg>
        <span>(+61) 400512836</span>
      </li>
      <li class="contacts__item">
        <svg class="contacts__icon" viewBox="0 0 24 24" aria-hidden="true">
          <rect x="2" y="5" width="20" height="14" rx="1.5" fill="#d11a24"/>
          <path d="M3 6l9 7 9-7" fill="none" stroke="#0d0d0d" stroke-width="1.8"/>
        </svg>
        <span>info@Q7RServices.example</span>
      </li>
      <li class="contacts__item">
        <svg class="contacts__icon" viewBox="0 0 24 24" aria-hidden="true">
          <g fill="none" stroke="#d11a24" stroke-width="1.8">
            <circle cx="12" cy="12" r="9.5"/>
            <ellipse cx="12" cy="12" rx="4" ry="9.5"/>
            <path d="M2.5 12h19M4 7h16M4 17h16"/>
          </g>
        </svg>
        <span>Q7RServices.example</span>
      </li>
    </ul>
  </section>

</main>
</body>
</html>
```